RMT Concreting and Excavation website design

We need a new webpage for our concreting business.

It just have the following pages
Home
Services
Galley
Online quote
FAQ
Contact

Examples are:
https://www.brookvaleworksbuild.example

Industry/Entity Type

Concreting

Font styles to use
Serif
Sans Serif

Colors
0054AA
0677BA
7BADD7
CADEEF
E8F1F8
0094D4
00A9DD
6FCCEA
C7EBF8
E9F6FB
59FF00
82FF00
B8FF75
E3FFCB
F4FFEA

Requirements
Should not have
• No shopping cart

```html
<!DOCTYPE html>
<html lang="en">
<head>
<meta charset="utf-8">
<title>RMT Concreting and Excavation</title>
<link href="https://fonts.googleapis.com/css2?family=Roboto:wght@400;500;700;900&display=swap" rel="stylesheet">
<style>
:root{
  --blue:#0054AA;
  --blue-mid:#0677BA;
  --blue-bright:#0094D4;
  --blue-pale:#E8F1F8;
  --blue-soft:#CADEEF;
  --green:#6DBE2E;
  --green-bright:#82D41A;
  --ink:#1b1b1b;
  --text:#555;
  --white:#fff;
  --dark:#111214;
}
*{box-sizing:border-box;margin:0;padding:0}
html,body{width:1200px;height:5216px;overflow:hidden}
body{font-family:"Roboto",sans-serif;color:var(--ink);background:var(--white);position:relative}
section,header,footer{position:relative;width:1200px;overflow:hidden}
.btn{display:inline-block;background:var(--green);color:#fff;font-weight:700;font-size:15px;text-transform:uppercase;padding:14px 30px;border-radius:3px;letter-spacing:.5px}
.section-title{font-size:40px;font-weight:900;text-transform:uppercase;text-align:center;color:var(--ink)}
.section-lead{font-size:16px;line-height:1.6;text-align:center;color:var(--text);width:640px;margin:14px auto 0}
.photo{position:absolute}

/* header */
.site-header{height:100px;background:#fff}
.brand{position:absolute;left:40px;top:10px;display:flex;align-items:center;gap:12px}
.brand-mark{width:56px;height:56px;border-radius:50%;background:var(--blue)}
.brand-name{font-size:19px;font-weight:700;color:var(--blue);line-height:1.15;width:150px}
.topbar{position:absolute;left:420px;top:0;width:780px;height:34px;background:var(--blue);clip-path:polygon(20px 0,100% 0,100% 100%,0 100%);display:flex;align-items:center;gap:28px;padding-left:120px;color:#fff;font-size:13px}
.topbar span{display:flex;align-items:center;gap:7px}
.topbar .top-phone{margin-left:auto;background:var(--green);height:34px;padding:0 26px;font-weight:700;font-size:15px}
.main-nav{position:absolute;left:410px;top:34px;height:66px;display:flex;align-items:center;gap:44px;font-size:15px;font-weight:700;text-transform:uppercase}
.main-nav a{color:var(--ink);text-decoration:none;position:relative}
.main-nav a.active{color:var(--green)}
.main-nav a.active::after{content:"";position:absolute;left:0;right:0;bottom:-22px;height:3px;background:var(--green)}
.quote-btn{position:absolute;right:40px;top:50px;border:2px solid var(--green);color:var(--green);font-size:14px;font-weight:700;padding:9px 22px;text-transform:uppercase}

/* hero */
.hero{height:700px}
.hero-photo{inset:0;background:linear-gradient(135deg,#6d5a46 0%,#9a8b7a 35%,#8d8c87 60%,#5e5246 100%)}
.hero-shade{position:absolute;inset:0;background:rgba(0,0,0,.28)}
.hero-content{position:absolute;left:0;right:0;top:290px;text-align:center;color:#fff}
.hero-content h1{font-size:44px;font-weight:900;text-transform:uppercase;letter-spacing:.5px}
.hero-content p{font-size:17px;line-height:1.5;width:540px;margin:14px auto 28px}
.dots{position:absolute;bottom:28px;left:0;right:0;display:flex;justify-content:center;gap:10px}
.dots i{width:10px;height:10px;border-radius:50%;background:rgba(255,255,255,.55)}
.dots i:first-child{background:#fff}

/* call band */
.call-band{height:200px;background:linear-gradient(90deg,var(--blue),var(--blue-mid));color:#fff}
.call-band h2{position:absolute;left:100px;top:46px;font-size:33px;font-weight:700;text-transform:uppercase}
.quick-form{position:absolute;left:100px;top:112px;display:flex;gap:14px}
.quick-form .field{width:182px;height:42px;background:#fff;color:#777;font-size:14px;padding:12px 12px;border-radius:2px;position:relative}
.quick-form .select::after{content:"";position:absolute;right:12px;top:17px;border:6px solid transparent;border-top-color:#444}
.quick-form .btn{height:42px;padding:12px 34px;width:190px;text-align:center}

/* services */
.services{height:540px}
.services .section-title{margin-top:70px}
.service-grid{position:absolute;left:100px;top:230px;display:flex;gap:14px}
.service-card{width:250px;height:310px;position:relative;overflow:hidden}
.service-card .photo{inset:0}
.service-card .shade{position:absolute;inset:0;background:linear-gradient(180deg,rgba(0,0,0,0) 45%,rgba(0,0,0,.55))}
.service-card.featured .shade{background:rgba(109,190,46,.88)}
.service-icon{position:absolute;left:104px;top:200px;width:42px;height:42px;border-radius:50%;background:var(--blue-mid);border:2px solid #fff}
.service-card h3{position:absolute;left:0;right:0;bottom:18px;text-align:center;color:#fff;font-size:15px;font-weight:700;text-transform:uppercase;line-height:1.2}
.service-card.featured .service-icon{top:36px;background:transparent}
.service-card.featured h3{top:92px;bottom:auto}
.service-card.featured p{position:absolute;left:22px;right:22px;top:124px;color:#fff;font-size:12px;line-height:1.5;text-align:center}

/* about */
.about{height:520px;background:var(--blue-pale)}
.about-text{position:absolute;left:100px;top:120px;width:500px}
.about-text .eyebrow{font-size:38px;font-weight:900;text-transform:uppercase}
.about-text h2{font-size:27px;font-weight:700;text-transform:uppercase;color:var(--ink);margin-top:2px}
.about-text p{font-size:15px;line-height:1.55;color:var(--text);margin-top:16px}
.about-actions{display:flex;align-items:center;gap:26px;margin-top:28px}
.about-actions .phone{display:flex;align-items:center;gap:10px;font-size:20px;font-weight:700}
.about-photo{left:690px;top:100px;width:410px;height:310px;background:linear-gradient(160deg,#b9c4cf 0%,#9a8f80 45%,#6e6656 100%)}
.since{position:absolute;left:655px;top:310px;width:160px;height:150px;background:var(--blue);color:#fff;text-align:center;padding-top:34px;border:6px solid #fff}
.since small{font-size:14px;font-weight:700;text-transform:uppercase;display:block}
.since strong{font-size:44px;font-weight:900;display:block;margin-top:4px}

/* gallery */
.gallery{height:1000px}
.gallery .section-title{margin-top:80px}
.gallery-grid{position:absolute;left:100px;top:230px;width:1000px;height:660px}
.gallery-grid .photo{border-radius:2px}
.g1{left:0;top:0;width:660px;height:320px;background:linear-gradient(160deg,#a7b0b8,#4d4e51 60%,#2f3033)}
.g2{left:672px;top:0;width:328px;height:320px;background:linear-gradient(170deg,#c9c5bf,#a19e98 60%,#8d8981)}
.g3{left:0;top:334px;width:326px;height:326px;background:linear-gradient(170deg,#c7d2dc,#b9aa95 55%,#8e8676)}
.g4{left:338px;top:334px;width:322px;height:326px;background:linear-gradient(170deg,#a9b9c6,#8c6a55 50%,#6b6a66)}
.g5{left:672px;top:334px;width:328px;height:326px;background:linear-gradient(170deg,#b0bcc7,#857d72 55%,#3f3d3a)}
.gallery .btn{position:absolute;left:500px;top:920px;width:200px;text-align:center}

/* clients */
.clients{height:720px;background:var(--blue-pale)}
.clients .section-title{margin-top:80px}
.testimonials{position:absolute;left:120px;top:245px;display:flex;gap:40px}
.testimonial{width:460px;height:330px;background:#fff;padding:36px 36px;position:relative;box-shadow:0 4px 14px rgba(0,60,120,.08)}
.testimonial h3{font-size:19px;font-weight:700;text-transform:uppercase}
.testimonial p{font-size:14px;line-height:1.6;color:var(--text);margin-top:14px}
.author{position:absolute;left:36px;bottom:40px;display:flex;align-items:center;gap:14px;font-size:14px;font-weight:700}
.avatar{width:40px;height:40px;border-radius:50%;background:var(--blue-soft)}
.quote-mark{position:absolute;right:34px;bottom:26px}
.arrow{position:absolute;top:390px}
.arrow.prev{left:62px}.arrow.next{right:62px}

/* news */
.news{height:620px}
.news .section-title{margin-top:40px}
.news-grid{position:absolute;left:100px;top:190px;display:flex;gap:26px}
.news-card{width:316px}
.news-photo{position:relative;height:200px}
.news-photo .photo{inset:0}
.date{position:absolute;left:14px;bottom:-14px;background:var(--green);color:#fff;font-size:12px;font-weight:700;padding:7px 14px;border-radius:2px;text-transform:uppercase}
.news-card h3{font-size:18px;font-weight:700;margin-top:34px;line-height:1.25}
.news-card p{font-size:13px;line-height:1.55;color:var(--text);margin-top:10px}
.news-card .more{font-size:13px;font-weight:700;margin-top:12px;display:block;text-transform:uppercase}

/* cta */
.cta{height:360px;background:linear-gradient(90deg,var(--blue) 0%,var(--blue-mid) 55%,var(--blue-bright) 100%);color:#fff}
.cta-photo{left:700px;top:0;width:500px;height:360px;background:linear-gradient(100deg,rgba(0,148,212,0) 0%,#3d6fa0 30%,#8a8a5a 70%,#d0a628 100%)}
.cta-text{position:absolute;left:100px;top:60px;width:640px}
.cta-text h3{font-size:25px;font-weight:700;text-transform:uppercase;white-space:nowrap}
.cta-text h2{font-size:38px;font-weight:900;text-transform:uppercase;margin-top:6px}
.cta-text p{font-size:15px;line-height:1.55;margin-top:14px;color:#e6f0fa;width:560px}
.cta-actions{display:flex;align-items:center;gap:26px;margin-top:24px}
.cta-actions .phone{display:flex;align-items:center;gap:10px;font-size:22px;font-weight:700}

/* footer */
.site-footer{height:456px;background:var(--dark);color:#ddd}
.foot-brand{position:absolute;left:100px;top:60px}
.foot-brand .brand-name{color:#fff;font-size:17px;width:160px;margin-top:12px}
.foot-brand .brand-mark{width:52px;height:52px}
.socials{display:flex;gap:10px;margin-top:22px}
.socials i{width:32px;height:32px;border-radius:50%;border:1.5px solid #888;display:block}
.foot-col{position:absolute;top:70px}
.foot-col h4{font-size:17px;font-weight:700;color:#fff;text-transform:uppercase;margin-bottom:18px}
.foot-col li{list-style:none;font-size:14px;line-height:2;color:#ccc}
.col-links{left:340px}
.col-contact{left:480px;width:250px}
.col-contact .row{display:flex;gap:10px;font-size:14px;line-height:1.5;margin-bottom:14px;color:#ccc}
.col-news{left:820px;width:290px}
.col-news p{font-size:14px;line-height:1.5;color:#ccc}
.subscribe{margin-top:18px;height:44px;background:#fff;border-radius:22px;position:relative;color:#888;font-size:14px;padding:13px 20px}
.subscribe b{position:absolute;right:3px;top:3px;width:38px;height:38px;border-radius:50%;background:var(--green)}
.copyright{position:absolute;left:0;right:0;bottom:0;height:56px;border-top:1px solid #2a2b2e;text-align:center;font-size:13px;line-height:56px;color:#aaa}
</style>
</head>
<body>

<header class="site-header">
  <div class="brand"><div class="brand-mark"></div><div class="brand-name">RMT Concreting &amp; Excavation</div></div>
  <div class="topbar">
    <span><svg width="12" height="16" viewBox="0 0 12 16"><path d="M6 0a6 6 0 0 0-6 6c0 4.5 6 10 6 10s6-5.5 6-10a6 6 0 0 0-6-6zm0 8.5a2.5 2.5 0 1 1 0-5 2.5 2.5 0 0 1 0 5z" fill="#fff"/></svg>Harbourside Way, ACT, Australia 2600</span>
    <span><svg width="14" height="14" viewBox="0 0 14 14"><circle cx="7" cy="7" r="6" fill="none" stroke="#fff" stroke-width="1.5"/><path d="M7 3.5V7l2.5 1.5" fill="none" stroke="#fff" stroke-width="1.5"/></svg>Mon - Fri 9am - 5pm</span>
    <span class="top-phone">+61 412 555 019</span>
  </div>
  <nav class="main-nav">
    <a class="active">Home</a><a>Services</a><a>Gallery</a><a>FAQ</a><a>Contact</a>
  </nav>
  <div class="quote-btn">Online Quote</div>
</header>

<section class="hero">
  <div class="photo hero-photo" role="img" aria-label="Workers levelling fresh concrete over steel mesh on a building site"></div>
  <div class="hero-shade"></div>
  <div class="hero-content">
    <h1>RMT Concreting &amp; Excavation</h1>
    <p>Reliable slabs, driveways and site works built to last, delivered on time by our local crew.</p>
    <span class="btn">Get a Quote</span>
  </div>
  <div class="dots"><i></i><i></i><i></i></div>
</section>

<section class="call-band">
  <h2>Call today +61 412 555 019 for a free consulation</h2>
  <div class="quick-form">
    <div class="field">Name</div>
    <div class="field">Phone</div>
    <div class="field">Email</div>
    <div class="field select">Services</div>
    <div class="btn">Get Started</div>
  </div>
</section>

<section class="services">
  <h2 class="section-title">Services We Provide</h2>
  <p class="section-lead">Lorem ipsum dolor sit amet, consectetur adipiscing elit, sed do eiusmod tempor incididunt ut labore et dolore magna aliqua. Quis ipsum suspendisse ultrices gravida.</p>
  <div class="service-grid">
    <div class="service-card">
      <div class="photo" style="background:linear-gradient(170deg,#8fb0d0,#c8a13a 55%,#6e5a3a)" role="img" aria-label="Yellow excavator digging at a site"></div>
      <div class="shade"></div><div class="service-icon"></div>
      <h3>Bulk &amp; Detailed<br>Excavation</h3>
    </div>
    <div class="service-card">
      <div class="photo" style="background:linear-gradient(170deg,#9fb7cc,#7a7f86 55%,#4a4c50)" role="img" aria-label="Civil works with machinery on a road"></div>
      <div class="shade"></div><div class="service-icon"></div>
      <h3>Civil Works</h3>
    </div>
    <div class="service-card featured">
      <div class="photo" style="background:linear-gradient(170deg,#7fae5a,#4d7a36)" role="img" aria-label="Landscaped garden area"></div>
      <div class="shade"></div><div class="service-icon"></div>
      <h3>Landscaping</h3>
      <p>Gardens, retaining walls and paving shaped to suit your block and finished with care.</p>
    </div>
    <div class="service-card">
      <div class="photo" style="background:linear-gradient(170deg,#c8c0b4,#a08f7a 55%,#6b5c4c)" role="img" aria-label="Worker finishing a concrete kerb"></div>
      <div class="shade"></div><div class="service-icon"></div>
      <h3>Concrete<br>Kerbing</h3>
    </div>
  </div>
</section>

<section class="about">
  <div class="about-text">
    <div class="eyebrow">About Us</div>
    <h2>RMT Concreting and Excavation</h2>
    <p>Sed ut perspiciatis unde omnis iste natus error sit volupta accusantium doloremque laudantium, totam rem aperiam, eaque ipsa quae ab illo inventore veritatis et quasi architecto beatae vitae.</p>
    <p>Sed ut perspiciatis unde omnis iste natus error sit volupta accusantium doloremque laudantium, totam rem aperiam, eaque ipsa quae ab illo inventore veritatis et quasi architecto beatae vitae.</p>
    <div class="about-actions">
      <span class="btn">Learn More</span>
      <span class="phone"><svg width="20" height="20" viewBox="0 0 24 24"><path d="M6.6 10.8a15 15 0 0 0 6.6 6.6l2.2-2.2a1 1 0 0 1 1-.25 11.4 11.4 0 0 0 3.6.57 1 1 0 0 1 1 1V20a1 1 0 0 1-1 1A17 17 0 0 1 3 4a1 1 0 0 1 1-1h3.5a1 1 0 0 1 1 1c0 1.250.2 2.45.57 3.6a1 1 0 0 1-.25 1z" fill="#0054AA"/></svg>+61 412 555 019</span>
    </div>
  </div>
  <div class="photo about-photo" role="img" aria-label="Crew laying a large concrete slab on site"></div>
  <div class="since"><small>Since</small><strong>1970</strong></div>
</section>

<section class="gallery">
  <h2 class="section-title">Our Gallery</h2>
  <p class="section-lead">Lorem ipsum dolor sit amet, consectetur adipiscing elit, sed do eiusmod tempor incididunt ut labore et dolore magna aliqua. Quis ipsum suspendisse ultrices gravida.</p>
  <div class="gallery-grid">
    <div class="photo g1" role="img" aria-label="Freshly laid concrete driveway curving past a garden"></div>
    <div class="photo g2" role="img" aria-label="Concrete slab in front of a house"></div>
    <div class="photo g3" role="img" aria-label="Concrete path beside a brick wall"></div>
    <div class="photo g4" role="img" aria-label="Driveway leading to a garage"></div>
    <div class="photo g5" role="img" aria-label="Smooth finished concrete surface"></div>
  </div>
  <span class="btn">View Our Work</span>
</section>

<section class="clients">
  <h2 class="section-title">Our Satisfied Clients</h2>
  <p class="section-lead">Lorem ipsum dolor sit amet, consectetur adipiscing elit, sed do eiusmod tempor incididunt ut labore et dolore magna aliqua. Quis ipsum suspendisse ultrices gravida.</p>
  <svg class="arrow prev" width="24" height="24" viewBox="0 0 24 24"><path d="M15 4l-8 8 8 8" fill="none" stroke="#333" stroke-width="2"/></svg>
  <svg class="arrow next" width="24" height="24" viewBox="0 0 24 24"><path d="M9 4l8 8-8 8" fill="none" stroke="#333" stroke-width="2"/></svg>
  <div class="testimonials">
    <div class="testimonial">
      <h3>Landscape contractor grants pass</h3>
      <p>We have used the team for several projects on our property and couldn't be happier. They arrived on time, kept the site tidy and explained every step clearly. The finished work looks great and it was done on budget, so we will call them again.</p>
      <div class="author"><span class="avatar"></span>Dana Merrow &amp; Colin Ashby</div>
      <svg class="quote-mark" width="44" height="36" viewBox="0 0 44 36"><path d="M0 36V20C0 8 6 2 16 0l2 5C12 7 9 11 9 16h9v20zm26 0V20C26 8 32 2 42 0l2 5c-6 2-9 6-9 11h9v20z" fill="#CADEEF"/></svg>
    </div>
    <div class="testimonial">
      <h3>Excavation work Jacksonville</h3>
      <p>The crew carried out a small grading job on one of the primary logging roads on our property. They were fast and found a drainage problem we had missed. They walked us through the fix and the road has held up well through the wet season.</p>
      <div class="author"><span class="avatar"></span>Dana Merrow &amp; Colin Ashby</div>
      <svg class="quote-mark" width="44" height="36" viewBox="0 0 44 36"><path d="M0 36V20C0 8 6 2 16 0l2 5C12 7 9 11 9 16h9v20zm26 0V20C26 8 32 2 42 0l2 5c-6 2-9 6-9 11h9v20z" fill="#CADEEF"/></svg>
    </div>
  </div>
</section>

<section class="news">
  <h2 class="section-title">Latest News</h2>
  <p class="section-lead">Lorem ipsum dolor sit amet, consectetur adipiscing elit, sed do eiusmod tempor incididunt ut labore et dolore magna aliqua. Quis ipsum suspendisse ultrices gravida.</p>
  <div class="news-grid">
    <article class="news-card">
      <div class="news-photo"><div class="photo" style="background:linear-gradient(170deg,#a8b4bf,#6f6e6c 55%,#45464a)" role="img" aria-label="Wet concrete driveway"></div><span class="date">June 4/2021</span></div>
      <h3>Section 1.10.32 of "de Finibus Bonorum et Malorum"</h3>
      <p>Sed ut perspiciatis unde omnis iste natus error sit voluptatem accusantium doloremque laudantium, totam rem aperiam.</p>
      <span class="more">Read More ›</span>
    </article>
    <article class="news-card">
      <div class="news-photo"><div class="photo" style="background:linear-gradient(170deg,#b7c3cc,#9a948a 55%,#77716a)" role="img" aria-label="Steel mesh laid out before a pour"></div><span class="date">June 4/2021</span></div>
      <h3>Section 1.10.32 of "de Finibus Bonorum et Malorum"</h3>
      <p>Sed ut perspiciatis unde omnis iste natus error sit voluptatem accusantium doloremque laudantium, totam rem aperiam.</p>
      <span class="more">Read More ›</span>
    </article>
    <article class="news-card">
      <div class="news-photo"><div class="photo" style="background:linear-gradient(170deg,#a9bccb,#8d6f55 55%,#5e564c)" role="img" aria-label="Excavated ground beside a house"></div><span class="date">June 4/2021</span></div>
      <h3>Section 1.10.32 of "de Finibus Bonorum et Malorum"</h3>
      <p>Sed ut perspiciatis unde omnis iste natus error sit voluptatem accusantium doloremque laudantium, totam rem aperiam.</p>
      <span class="more">Read More ›</span>
    </article>
  </div>
</section>

<section class="cta">
  <div class="photo cta-photo" role="img" aria-label="Site manager holding plans in front of a yellow excavator"></div>
  <div class="cta-text">
    <h3>Starting your own concreting business?</h3>
    <h2>We're here to help</h2>
    <p>Sed ut perspiciatis unde omnis iste natus error sit volupta accusantium doloremque laudantium, totam rem aperiam, eaque ipsa quae ab illo inventore veritatis et quasi architecto beatae vitae dicta sunt.</p>
    <div class="cta-actions">
      <span class="btn">Contact Us</span>
      <span class="phone"><svg width="22" height="22" viewBox="0 0 24 24"><path d="M6.6 10.8a15 15 0 0 0 6.6 6.6l2.2-2.2a1 1 0 0 1 1-.25 11.4 11.4 0 0 0 3.6.57 1 1 0 0 1 1 1V20a1 1 0 0 1-1 1A17 17 0 0 1 3 4a1 1 0 0 1 1-1h3.5a1 1 0 0 1 1 1c0 1.25.2 2.45.57 3.6a1 1 0 0 1-.25 1z" fill="#fff"/></svg>541-555-0147</span>
    </div>
  </div>
</section>

<footer class="site-footer">
  <div class="foot-brand">
    <div class="brand-mark"></div>
    <div class="brand-name">RMT Concreting &amp; Excavation</div>
    <div class="socials"><i></i><i></i><i></i><i></i></div>
  </div>
  <div class="foot-col col-links">
    <h4>Quick Link</h4>
    <ul><li>Home</li><li>Services</li><li>Gallery</li><li>Online quote</li><li>FAQ</li><li>Contact</li></ul>
  </div>
  <div class="foot-col col-contact">
    <h4>Contact Us</h4>
    <div class="row"><svg width="12" height="16" viewBox="0 0 12 16"><path d="M6 0a6 6 0 0 0-6 6c0 4.5 6 10 6 10s6-5.5 6-10a6 6 0 0 0-6-6zm0 8.5a2.5 2.5 0 1 1 0-5 2.5 2.5 0 0 1 0 5z" fill="#6DBE2E"/></svg><span>Harbourside Way, ACT,<br>Australia 2600</span></div>
    <div class="row"><svg width="16" height="12" viewBox="0 0 16 12"><rect x=".75" y=".75" width="14.5" height="10.5" fill="none" stroke="#6DBE2E" stroke-width="1.5"/><path d="M1 1l7 6 7-6" fill="none" stroke="#6DBE2E" stroke-width="1.5"/></svg><span>Email:<br>hello@rmtconcreting.example</span></div>
    <div class="row"><svg width="14" height="14" viewBox="0 0 24 24"><path d="M6.6 10.8a15 15 0 0 0 6.6 6.6l2.2-2.2a1 1 0 0 1 1-.25 11.4 11.4 0 0 0 3.6.57 1 1 0 0 1 1 1V20a1 1 0 0 1-1 1A17 17 0 0 1 3 4a1 1 0 0 1 1-1h3.5a1 1 0 0 1 1 1c0 1.25.2 2.45.57 3.6a1 1 0 0 1-.25 1z" fill="#6DBE2E"/></svg><span>Phone:<br>+61 412 555 019</span></div>
  </div>
  <div class="foot-col col-news">
    <h4>Our Newsletter</h4>
    <p>Sign up to stay in the loop with RMT Concreting and Excavation.</p>
    <div class="subscribe">Enter Email<b></b></div>
  </div>
  <div class="copyright">Copyright © 2021 RMT Concreting and Excavation. All rights</div>
</footer>

</body>
</html>
```